Upscale business cards needed for family office

We would like professional business cards created for employees of our family office. Relatively simple and straightforward, but also with a unique element to set them apart. Probably stick with neutral and simple colors that mesh well with the colors in the logo. We need space for the traditional elements, including name, title, address, email/phone number.

Industry/Entity Type

Business

Contact Information for Business Card

Space for name, title, phone number, email, address

```html
<!DOCTYPE html>
<html lang="en">
<head>
<meta charset="utf-8">
<title>Family Office Business Card</title>
<link rel="stylesheet" href="https://fonts.googleapis.com/css2?family=Carlito:wght@700&display=swap">
<style>
  :root {
    --page: #ffffff;
    --frame-line: #000000;
    --frame-gap: #ffffff;
    --text: #333333;
    --sky-blue: #8fc0f2;
    --sky-cyan: #b8ecf6;
    --sky-sand: #f3e6bf;
    --sky-cloud: #d6d6d8;
    --sky-grey: #c4c6c9;
    --tab-blue: #b5d6f6;
    --tab-grey: #c3c4c6;
  }
  * { margin: 0; padding: 0; box-sizing: border-box; }
  html, body {
    width: 1200px;
    height: 815px;
    overflow: hidden;
    background: var(--page);
  }
  .card {
    position: relative;
    width: 1200px;
    height: 815px;
  }
  .card-frame {
    position: absolute;
    inset: 0;
    width: 1200px;
    height: 815px;
  }
  .contact-block {
    position: absolute;
    left: 140px;
    top: 229px;
    font-family: "Carlito", "Calibri", sans-serif;
    font-weight: 700;
    font-size: 37px;
    line-height: 54.5px;
    color: var(--text);
    list-style: none;
  }
</style>
</head>
<body>
  <div class="card">
    <svg class="card-frame" viewBox="0 0 1080 733.5" preserveAspectRatio="none" xmlns="http://www.w3.org/2000/svg">
      <defs>
        <linearGradient id="sky-base" x1="0" y1="0" x2="0" y2="1">
          <stop offset="0" stop-color="var(--sky-blue)"/>
          <stop offset="0.5" stop-color="#b2d0f0"/>
          <stop offset="0.75" stop-color="var(--sky-cloud)"/>
          <stop offset="1" stop-color="var(--sky-grey)"/>
        </linearGradient>
        <radialGradient id="sky-glow" cx="0.2" cy="0.3" r="0.45">
          <stop offset="0" stop-color="var(--sky-cyan)" stop-opacity="0.95"/>
          <stop offset="1" stop-color="var(--sky-cyan)" stop-opacity="0"/>
        </radialGradient>
        <radialGradient id="sky-sun" cx="0.05" cy="0.75" r="0.3">
          <stop offset="0" stop-color="var(--sky-sand)" stop-opacity="0.9"/>
          <stop offset="1" stop-color="var(--sky-sand)" stop-opacity="0"/>
        </radialGradient>
      </defs>

      <path class="frame-outline" fill="var(--frame-gap)" stroke="var(--frame-line)" stroke-width="5" stroke-linejoin="miter"
        d="M168 145 H900 V175 H918 V190 H962 V510 H918 V525 H900 V555 H168 V525 H148 V510 H104 V190 H148 V175 H168 Z"/>

      <g class="sky-painting" role="img" aria-label="Soft watercolour sky in pale blue, cyan and cloud grey">
        <path fill="url(#sky-base)"
          d="M176 153 H892 V183 H910 V198 H952 V500 H910 V517 H892 V548 H176 V517 H156 V500 H114 V198 H156 V183 H176 Z"/>
        <path fill="url(#sky-glow)"
          d="M176 153 H892 V183 H910 V198 H952 V500 H910 V517 H892 V548 H176 V517 H156 V500 H114 V198 H156 V183 H176 Z"/>
        <path fill="url(#sky-sun)"
          d="M176 153 H892 V183 H910 V198 H952 V500 H910 V517 H892 V548 H176 V517 H156 V500 H114 V198 H156 V183 H176 Z"/>
      </g>

      <g class="corner-tabs" stroke="var(--frame-line)" stroke-width="4">
        <rect x="120" y="157" width="26" height="16" fill="var(--tab-blue)"/>
        <rect x="920" y="157" width="26" height="16" fill="var(--tab-blue)"/>
        <rect x="120" y="527" width="26" height="16" fill="var(--tab-grey)"/>
        <rect x="920" y="527" width="26" height="16" fill="var(--tab-grey)"/>
      </g>
    </svg>

    <ul class="contact-block">
      <li class="contact-name">Name,</li>
      <li class="contact-title">Title,</li>
      <li class="contact-phone">Phone number,</li>
      <li class="contact-email-address">email, address</li>
    </ul>
  </div>
</body>
</html>
```